2 banners brivon brand stories / tools / gastronomy

We need 2 banners each for the brand stories on Brivon.
The banners should have the following formats:
(1464px x 625px and 463px x 625px).
2x banner for the brand plomin
2x banners for the brand KALDUR
The banner should be relatively neutral with the logo. Like the example I uploaded.

Brivon

```html
<!DOCTYPE html>
<html lang="en">
<head>
<meta charset="utf-8">
<title>Brivon brand story banners – plomin and KALDUR</title>
<link rel="stylesheet" href="https://fonts.googleapis.com/css2?family=Orbitron:wght@500&display=swap">
<style>
  :root {
    --canvas: #ffffff;
    --ink: #111111;
    --night: #000000;
    --wedge: #231f20;
    --edge: #5a5a5a;
    --steel-light: #f0f0f0;
    --steel-mid: #9a9a9b;
    --steel-dark: #58595b;
    --logo-light: #ffffff;
  }
  html, body {
    margin: 0;
    padding: 0;
    width: 1200px;
    height: 1000px;
    overflow: hidden;
    background: var(--canvas);
  }
  .canvas {
    position: relative;
    width: 1200px;
    height: 1000px;
  }
  .banner {
    position: absolute;
    display: block;
  }
  .banner--wide { width: 710px; height: 303px; left: 78px; }
  .banner--tall { width: 225px; height: 303px; left: 902px; }
  .row--plomin { top: 136px; }
  .row--kaldur { top: 600px; }
  .brand-name {
    font-family: "Orbitron", sans-serif;
    font-weight: 500;
  }
  .brand-name--dark { fill: var(--ink); }
  .brand-name--light { fill: var(--logo-light); }
  .brand-mark { fill: none; stroke: var(--ink); stroke-width: 2.4; }
  .brand-mark--light { stroke: var(--logo-light); stroke-width: 1; }
</style>
</head>
<body>
<main class="canvas">

  <svg width="0" height="0" style="position:absolute" aria-hidden="true">
    <defs>
      <linearGradient id="steel-field" x1="0" y1="1" x2="0.75" y2="0.1">
        <stop offset="0" stop-color="var(--steel-light)"/>
        <stop offset="0.55" stop-color="var(--steel-mid)"/>
        <stop offset="1" stop-color="var(--steel-dark)"/>
      </linearGradient>
      <linearGradient id="steel-band" x1="0" y1="0" x2="1" y2="1">
        <stop offset="0" stop-color="#bcbdbf"/>
        <stop offset="0.55" stop-color="#6d6e70"/>
        <stop offset="1" stop-color="#1a1a1a"/>
      </linearGradient>
      <linearGradient id="night-field" x1="0" y1="0" x2="1" y2="1">
        <stop offset="0" stop-color="#1c1c1c"/>
        <stop offset="0.5" stop-color="#000"/>
        <stop offset="1" stop-color="#000"/>
      </linearGradient>
      <linearGradient id="chrome-edge" x1="0" y1="0" x2="1" y2="1">
        <stop offset="0" stop-color="#cfcfcf"/>
        <stop offset="0.5" stop-color="#ffffff"/>
        <stop offset="1" stop-color="#3a3a3a"/>
      </linearGradient>
      <linearGradient id="tall-field" x1="0" y1="1" x2="1" y2="0.3">
        <stop offset="0" stop-color="var(--steel-light)"/>
        <stop offset="0.6" stop-color="#7d7e80"/>
        <stop offset="1" stop-color="#3c3c3d"/>
      </linearGradient>
    </defs>
  </svg>

  <!-- plomin wide -->
  <svg class="banner banner--wide row--plomin" viewBox="0 0 710 303" aria-label="plomin brand story banner, wide">
    <rect width="710" height="303" fill="url(#steel-field)"/>
    <polygon points="152,0 277,0 590,303 470,303" fill="url(#steel-band)"/>
    <polygon points="185,20 300,135 335,147 375,152 450,210 400,210 330,160 262,128" fill="var(--steel-dark)" opacity="0.85"/>
    <polygon points="375,205 470,303 493,303 395,205" fill="#c8c8c8" opacity="0.6"/>
    <polygon points="277,0 710,0 710,303 590,303" fill="url(#night-field)"/>
    <line x1="277" y1="0" x2="590" y2="303" stroke="url(#chrome-edge)" stroke-width="2"/>
    <polygon points="700,2 552,152 700,302" fill="var(--wedge)" stroke="var(--edge)" stroke-width="6"/>
    <text class="brand-name brand-name--dark" x="32" y="44" font-size="24">plomin</text>
  </svg>

  <!-- plomin tall -->
  <svg class="banner banner--tall row--plomin" viewBox="0 0 225 303" aria-label="plomin brand story banner, tall">
    <rect width="225" height="303" fill="var(--night)"/>
    <polygon points="0,72 220,303 0,303" fill="url(#tall-field)"/>
    <line x1="0" y1="72" x2="222" y2="303" stroke="url(#chrome-edge)" stroke-width="5"/>
    <line x1="6" y1="100" x2="210" y2="303" stroke="#2a2a2a" stroke-width="3" opacity="0.7"/>
    <polygon points="225,6 124,106 225,207" fill="var(--wedge)" stroke="var(--edge)" stroke-width="4"/>
    <text class="brand-name brand-name--light" x="10" y="20" font-size="11">plomin</text>
  </svg>

  <!-- KALDUR wide -->
  <svg class="banner banner--wide row--kaldur" viewBox="0 0 710 303" aria-label="KALDUR brand story banner, wide">
    <rect width="710" height="303" fill="url(#steel-field)"/>
    <polygon points="152,0 277,0 590,303 470,303" fill="url(#steel-band)"/>
    <polygon points="185,20 300,135 335,147 375,152 450,210 400,210 330,160 262,128" fill="var(--steel-dark)" opacity="0.85"/>
    <polygon points="375,205 470,303 493,303 395,205" fill="#c8c8c8" opacity="0.6"/>
    <polygon points="277,0 710,0 710,303 590,303" fill="url(#night-field)"/>
    <line x1="277" y1="0" x2="590" y2="303" stroke="url(#chrome-edge)" stroke-width="2"/>
    <polygon points="700,2 552,152 700,302" fill="var(--wedge)" stroke="var(--edge)" stroke-width="6"/>
    <circle class="brand-mark" cx="21" cy="35" r="9"/>
    <text class="brand-name brand-name--dark" x="36" y="42" font-size="18" letter-spacing="2">KALDUR</text>
  </svg>

  <!-- KALDUR tall -->
  <svg class="banner banner--tall row--kaldur" viewBox="0 0 225 303" aria-label="KALDUR brand story banner, tall">
    <rect width="225" height="303" fill="var(--night)"/>
    <polygon points="0,72 220,303 0,303" fill="url(#tall-field)"/>
    <line x1="0" y1="72" x2="222" y2="303" stroke="url(#chrome-edge)" stroke-width="5"/>
    <line x1="6" y1="100" x2="210" y2="303" stroke="#2a2a2a" stroke-width="3" opacity="0.7"/>
    <polygon points="225,6 124,106 225,207" fill="var(--wedge)" stroke="var(--edge)" stroke-width="4"/>
    <circle class="brand-mark brand-mark--light" cx="13" cy="16" r="3.2"/>
    <text class="brand-name brand-name--light" x="19" y="19" font-size="7.5" letter-spacing="0.8">KALDUR</text>
  </svg>

</main>
</body>
</html>
```